Sales Process

I need a card/page to hand out to my new clients that gives them an over view of our sales process start to finish. Along with 3 points that set us apart from all other competition.
The attached file is my first attempt with other ideas so give your suggestions.
Check out my website to get an idea of who we are. www.brightmeadowyards.com

```html
<!DOCTYPE html>
<html lang="en">
<head>
<meta charset="utf-8">
<title>Bright Meadow Yards — Our Process</title>
<link rel="stylesheet" href="https://fonts.googleapis.com/css2?family=Open+Sans:ital,wght@0,400;0,600;0,700;1,400&display=swap">
<style>
  :root {
    --paper-center: #f7f7f7;
    --paper-edge: #e3e4e6;
    --ink: #1f1f26;
    --road-dark: #555557;
    --leaf-green: #8cc63f;
    --sun-orange: #eea526;
    --disc: #e9e9ea;
    --disc-rim: #f5f5f5;
    --white: #ffffff;
  }
  html, body {
    margin: 0;
    width: 1200px;
    height: 928px;
    overflow: hidden;
  }
  body {
    background: radial-gradient(ellipse at 50% 50%, var(--paper-center) 0%, var(--paper-edge) 100%);
    font-family: "Open Sans", sans-serif;
  }
  .process-card {
    display: block;
    width: 1200px;
    height: 928px;
  }
  .road { fill: none; stroke-width: 60; }
  .road--dark { stroke: var(--road-dark); }
  .road--green { stroke: var(--leaf-green); }
  .step-disc-rim { fill: var(--disc-rim); }
  .step-disc { fill: var(--disc); }
  .accent-arc { fill: none; stroke-width: 6; }
  .accent-arc--green { stroke: var(--leaf-green); }
  .accent-arc--dark { stroke: var(--road-dark); }
  .callout-line { fill: none; stroke-width: 4; }
  .callout-line--green { stroke: var(--leaf-green); }
  .callout-line--dark { stroke: var(--road-dark); }
  .callout-dot { stroke-width: 5; fill: var(--white); }
  .callout-dot--green { stroke: var(--leaf-green); }
  .callout-dot--dark { stroke: var(--road-dark); }
  .step-title {
    font-family: "Open Sans", sans-serif;
    font-weight: 700;
    font-size: 37px;
    fill: var(--ink);
  }
  .finale-title {
    font-family: "Open Sans", sans-serif;
    font-weight: 700;
    font-size: 45px;
    fill: var(--ink);
  }
  .finale-title--green { fill: var(--leaf-green); }
  .bullet-text {
    font-family: "Open Sans", sans-serif;
    font-weight: 600;
    font-size: 23px;
    fill: var(--ink);
  }
  .icon-green { fill: var(--leaf-green); }
  .icon-dark { fill: var(--road-dark); }
  .sun-disc { fill: var(--sun-orange); }
  .sun-core { fill: var(--white); }
  .brand-name {
    font-family: "Open Sans", sans-serif;
    font-weight: 700;
    font-size: 46px;
    fill: var(--road-dark);
  }
  .brand-tagline {
    font-family: "Open Sans", sans-serif;
    font-style: italic;
    font-size: 20px;
    fill: var(--ink);
  }
</style>
</head>
<body>
<svg class="process-card" viewBox="0 0 1940 1372" preserveAspectRatio="xMidYMid meet" role="group" aria-label="Our process from first call to finished yard">

  <!-- Key points -->
  <g class="key-points">
    <text class="bullet-text" x="90" y="166">•</text>
    <text class="bullet-text" x="116" y="166">Lorem ipsum dolor sit amet, consectetur adipiscing elit, sed do</text>
    <text class="bullet-text" x="90" y="210">•</text>
    <text class="bullet-text" x="116" y="210">Lorem ipsum dolor sit amet, consectetur adipiscing elit,</text>
    <text class="bullet-text" x="90" y="254">•</text>
    <text class="bullet-text" x="116" y="254">Lorem ipsum dolor sit amet, consectetur adipiscing elit, sed do</text>
  </g>

  <!-- Winding road -->
  <g class="road-path">
    <path class="road road--green" d="M116 1099 A160 160 0 0 0 411 1087"/>
    <path class="road road--dark" d="M411 1087 A160 160 0 0 0 405.5 964.5 A160 160 0 0 1 695 828.5 A160 160 0 0 0 785 910"/>
    <path class="road road--green" d="M785 910 A160 160 0 0 0 985 828"/>
    <path class="road road--dark" d="M985 828 A160 160 0 0 0 986.5 696 A160 160 0 0 1 1278.5 562 A160 160 0 0 0 1311 605"/>
    <path class="road road--green" d="M1311 605 A160 160 0 0 0 1584 492 C1584 420 1548 390 1556 330 C1560 300 1572 285 1592 270"/>
  </g>

  <!-- Step discs -->
  <g class="step-discs">
    <circle class="step-disc-rim" cx="261" cy="1032" r="124"/>
    <circle class="step-disc" cx="261" cy="1032" r="116"/>
    <circle class="step-disc-rim" cx="550" cy="897" r="124"/>
    <circle class="step-disc" cx="550" cy="897" r="116"/>
    <circle class="step-disc-rim" cx="840" cy="760" r="124"/>
    <circle class="step-disc" cx="840" cy="760" r="116"/>
    <circle class="step-disc-rim" cx="1133" cy="632" r="124"/>
    <circle class="step-disc" cx="1133" cy="632" r="116"/>
    <circle class="sun-disc" cx="1424" cy="492" r="118"/>
  </g>

  <!-- Accent arcs -->
  <g class="accent-arcs">
    <path class="accent-arc accent-arc--green" d="M139 1032 A122 122 0 0 1 261 910"/>
    <path class="accent-arc accent-arc--dark" d="M674 897 A124 124 0 0 1 550 1021"/>
    <path class="accent-arc accent-arc--green" d="M732 708 A124 124 0 0 1 892 648"/>
    <path class="accent-arc accent-arc--dark" d="M1257 632 A124 124 0 0 1 1133 756"/>
    <path class="accent-arc accent-arc--green" d="M1314 438 A124 124 0 0 1 1476 378"/>
  </g>

  <!-- Step icons -->
  <g class="step-icons">
    <circle class="icon-green" cx="261" cy="1030" r="50" role="img" aria-label="Icon: support agent with headset"/>
    <rect class="icon-dark" x="490" y="840" width="120" height="118" rx="14" role="img" aria-label="Icon: team meeting with speech bubbles"/>
    <rect class="icon-green" x="796" y="698" width="94" height="122" rx="8" role="img" aria-label="Icon: proposal document with pencil"/>
    <rect class="icon-dark" x="1074" y="558" width="120" height="134" rx="40" role="img" aria-label="Icon: hard hat over a gear"/>
    <circle class="sun-core" cx="1424" cy="492" r="68" role="img" aria-label="Icon: happy customer emblem"/>
  </g>

  <!-- Callout: initial call -->
  <g class="callout callout--initial">
    <path class="callout-line callout-line--green" d="M84 740 V1029 H141"/>
    <circle class="callout-dot callout-dot--green" cx="84" cy="727" r="12"/>
    <text class="step-title" x="116" y="740">INITIAL</text>
    <text class="step-title" x="116" y="785">CALL.</text>
    <text class="step-title" x="116" y="830">CAN WE</text>
    <text class="step-title" x="116" y="875">HELP?</text>
  </g>

  <!-- Callout: site visit -->
  <g class="callout callout--site-visit">
    <path class="callout-line callout-line--dark" d="M554 1021 V1255 H618"/>
    <circle class="callout-dot callout-dot--dark" cx="630" cy="1255" r="12"/>
    <text class="step-title" x="586" y="1112">SITE VISIT,</text>
    <text class="step-title" x="586" y="1156">DISCUSS,</text>
    <text class="step-title" x="586" y="1200">PLAN,VISIT</text>
  </g>

  <!-- Callout: design proposal -->
  <g class="callout callout--design">
    <path class="callout-line callout-line--green" d="M671 468 V706 H735"/>
    <circle class="callout-dot callout-dot--green" cx="671" cy="455" r="12"/>
    <text class="step-title" x="704" y="467">DESIGN</text>
    <text class="step-title" x="704" y="512">PROPOSAL</text>
  </g>

  <!-- Callout: installation -->
  <g class="callout callout--installation">
    <path class="callout-line callout-line--dark" d="M1134 756 V985 H1198"/>
    <circle class="callout-dot callout-dot--dark" cx="1210" cy="985" r="12"/>
    <text class="step-title" x="1170" y="868">INSTALLATION</text>
    <text class="step-title" x="1170" y="912">CONSTRUCTION</text>
  </g>

  <!-- Callout: complete -->
  <g class="callout callout--complete">
    <path class="callout-line callout-line--green" d="M1256 125 V440 H1318"/>
    <circle class="callout-dot callout-dot--green" cx="1256" cy="112" r="12"/>
    <text class="finale-title finale-title--green" x="1288" y="131">COMPLETE</text>
    <text class="finale-title" x="1288" y="186">KICKBACK + RELAY WITH</text>
    <text class="finale-title" x="1288" y="241">SMILE ON YOUR FACE</text>
  </g>

  <!-- Brand -->
  <g class="brand">
    <text class="brand-name" x="1633" y="1210" text-anchor="middle">Bright Meadow Yards</text>
    <text class="brand-tagline" x="1636" y="1297" text-anchor="middle">Creating Exceptional Outdoor Living Spaces</text>
  </g>
</svg>
</body>
</html>
```